Lionel's UPDATE -Across the Board

Insurance Agent Business card and probably everything else !
Been in business for over 35 years and never took the time to update so really like the black-gold combo but open for suggestions (Honestly, I have NO idea how this works but sounds very cool ) Attached are two samples that I enjoy. The black and gold option is my favorite so looking for something like that!

```html
<!DOCTYPE html>
<html lang="en">
<head>
<meta charset="utf-8">
<title>Lionel R Hartley – Business Card</title>
<link rel="stylesheet" href="https://fonts.googleapis.com/css2?family=Crimson+Pro:ital,wght@0,400;0,600;1,400&display=swap">
<style>
  :root {
    --page: #ffffff;
    --black: #000000;
    --charcoal: #151515;
    --gold: #c9a264;
    --gold-light: #e6d29a;
    --gold-dark: #7a5424;
    --silver: #b9b3ae;
    --silver-dark: #3a3a3a;
  }
  * { margin: 0; padding: 0; box-sizing: border-box; }
  html, body {
    width: 1200px; height: 1000px; overflow: hidden;
    background: var(--page);
    font-family: "Crimson Pro", "Palatino Linotype", serif;
  }
  .card {
    position: absolute; left: 246px;
    width: 714px; height: 407px;
    background: var(--charcoal);
    overflow: hidden;
    color: var(--gold);
  }
  .card--front { top: 78px; }
  .card--back { top: 521px; }

  .card__black { position: absolute; left: 0; width: 100%; background: var(--black); }
  .card--front .card__black { top: 0; height: 112px; }
  .card--back .card__black { top: 300px; height: 107px; }

  .ribbon-band {
    position: absolute; left: 0; width: 100%; height: 76px;
    background: linear-gradient(90deg, var(--gold-dark) 0%, var(--gold) 25%, #a0804e 55%, #6e6a66 78%, var(--silver-dark) 100%);
  }
  .card--front .ribbon-band { top: 112px; }
  .card--back .ribbon-band {
    top: 224px;
    background: linear-gradient(90deg, var(--silver-dark) 0%, #6e6a66 22%, #a0804e 45%, var(--gold) 75%, var(--gold-dark) 100%);
  }

  .brand {
    position: absolute; text-align: center; line-height: 1;
    font-weight: 400; letter-spacing: 1px; color: var(--gold);
  }
  .card--front .brand { left: 117px; width: 120px; top: 96px; font-size: 23px; }
  .card--front .brand { top: 36px; }
  .card--back .brand { left: 0; width: 714px; top: 130px; font-size: 42px; }

  .identity { position: absolute; left: 57px; top: 240px; width: 240px; text-align: center; }
  .identity__name { font-size: 38px; line-height: 40px; color: var(--gold); font-weight: 400; white-space: nowrap; }
  .identity__role { font-size: 17px; line-height: 20px; margin-top: 6px; white-space: nowrap; }
  .identity__est { font-size: 13.5px; line-height: 16px; font-style: italic; margin-top: 1px; }

  .contacts { position: absolute; left: 440px; top: 200px; list-style: none; font-size: 16.5px; line-height: 20px; color: var(--gold-light); }
  .contacts li { display: flex; align-items: flex-start; }
  .contacts li + li { margin-top: 19px; }
  .contacts li:nth-child(3) { margin-top: 16px; }
  .contacts svg { width: 22px; height: 22px; margin-right: 13px; flex: none; }

  .website {
    position: absolute; left: 0; width: 714px; top: 340px; text-align: center;
    font-size: 21px; line-height: 28px; font-weight: 600; color: var(--gold-light); letter-spacing: 0.3px;
  }
</style>
</head>
<body>

<section class="card card--front">
  <div class="card__black"></div>
  <div class="ribbon-band" role="img" aria-label="Flowing gold and silver ribbon band"></div>

  <div class="brand">LRH</div>

  <div class="identity">
    <h1 class="identity__name">Lionel R Hartley</h1>
    <p class="identity__role">Insurance &amp; Financial Consultant</p>
    <p class="identity__est">Est. 1985</p>
  </div>

  <ul class="contacts">
    <li>
      <svg viewBox="0 0 24 24" aria-hidden="true"><circle cx="12" cy="12" r="12" fill="var(--gold-light)"/><rect x="6" y="8" width="12" height="8" rx="1" fill="none" stroke="#151515" stroke-width="1.6"/><path d="M6.5 8.5 L12 13 L17.5 8.5" fill="none" stroke="#151515" stroke-width="1.6"/></svg>
      <span>lionel@lrhinsures.com</span>
    </li>
    <li>
      <svg viewBox="0 0 24 24" aria-hidden="true"><circle cx="12" cy="12" r="12" fill="var(--gold-light)"/><path d="M8.5 6 C7 7 7 9.5 9 12.5 C11 15.5 13.5 17.5 15.5 17.5 C16.5 17.5 17.5 16.5 17.5 16 L15.5 14 L14 15 C12.5 14.5 10.5 12 10 10.5 L11 9 L9.5 6 Z" fill="#151515"/></svg>
      <span>954-555-0142<br>954-555-0187</span>
    </li>
    <li>
      <svg viewBox="0 0 24 24" aria-hidden="true"><circle cx="12" cy="12" r="12" fill="var(--gold-light)"/><path d="M12 5 C9 5 7.5 7.2 7.5 9.5 C7.5 13 12 19 12 19 C12 19 16.5 13 16.5 9.5 C16.5 7.2 15 5 12 5 Z" fill="#151515"/><circle cx="12" cy="9.6" r="2" fill="var(--gold-light)"/></svg>
      <span>4120 Harbor View Drive,<br>Suite 210<br>Coral Shores,<br>FL 33099</span>
    </li>
  </ul>
</section>

<section class="card card--back">
  <div class="ribbon-band" role="img" aria-label="Flowing silver and gold ribbon band"></div>
  <div class="card__black"></div>

  <div class="brand">LRH</div>
  <p class="website">www.lrhinsures.com</p>
</section>

</body>
</html>
```